Label Redesign For Hemp Oil Tincture Bottle*

I need a label redesigned for Marbleleaf Hemp, current bottle label and logo is attached. The current label doesn't standout, not sure if its the font size or colors on the existing label. It is very important to have on the label that this is a Premium Full Spectrum Hemp Oil that is 2000mg. Then after the label is redesigned and approved, I would need to packaging to be designed to match the approved label design.
This Hemp oil has a relaxing effect to help ease mental and emotional stress, tension and worry. The Omega Fatty Acids it contains also naturally improves your mood and overall brain function, causing you to feel more alert and focused. Hemp Oil helps with insomnia. Take some 2-3 hours before bedtime, you will feel relaxed yet aware of how tired you are that it will lead to a good night's sleep. Hemp Oil helps ease chronic pain and inflammation from conditions such as arthritis, fibromyalgia, lupus, and MS. As a pain relief supplement, it is a safer, natural, non-chemical and non-addictive alternative to prescription painkillers.

Target Market(s)

Adults

Industry/Entity Type

Supplement

Font styles to use
Serif
Sans Serif

Colors

Designer to choose colors to be used in the design.

Requirements
Must have
• All information thats on current label but where it says 750 in the front of the existing label, it needs to say 2000. The 2000 should be prominent on the label.

```html
<!DOCTYPE html>
<html lang="en">
<head>
<meta charset="UTF-8">
<title>Marbleleaf Hemp – Full Spectrum Hemp Oil Label</title>
<link rel="stylesheet" href="https://fonts.googleapis.com/css2?family=Lato:wght@400;700;900&family=Roboto+Condensed:wght@700&display=swap">
<style>
  :root {
    --canvas: #ffffff;
    --cream: #eeeed4;
    --ink: #121212;
    --leaf: #b3cb8a;
    --leaf-deep: #9fbb73;
    --paper: #ffffff;
    --stone: #55554f;
  }
  * { box-sizing: border-box; margin: 0; padding: 0; }
  html, body {
    width: 1014px; height: 1200px; overflow: hidden;
    background: var(--canvas);
  }
  .canvas { position: relative; width: 1014px; height: 1200px; }

  .label {
    position: absolute; left: 118px; top: 106px;
    width: 777px; height: 987px;
    background: var(--ink);
    border: 3px solid var(--ink);
    font-family: "Lato", sans-serif;
    overflow: hidden;
  }

  /* top cream band */
  .label__band-top {
    position: absolute; left: 0; top: 0; width: 100%; height: 368px;
    background: var(--cream);
    border-bottom: 6px solid var(--ink);
  }
  .label__divider {
    position: absolute; left: 124px; top: 0; width: 4px; height: 100%;
    background: var(--ink);
  }
  .label__vertical {
    position: absolute; left: 0; width: 124px;
    display: flex; align-items: center; justify-content: center;
  }
  .label__vertical span {
    writing-mode: vertical-rl; transform: rotate(180deg);
    font-weight: 900; letter-spacing: 6px; white-space: nowrap;
  }
  .label__vertical--hemp { top: 0; height: 362px; }
  .label__vertical--hemp span { color: var(--ink); font-size: 52px; }
  .label__vertical--brand { top: 368px; height: 619px; }
  .label__vertical--brand span { color: var(--paper); font-size: 46px; letter-spacing: 7px; }

  .brand-name {
    position: absolute; left: 128px; width: 428px; top: 0; height: 362px;
    display: flex; align-items: center; justify-content: center; gap: 14px;
  }
  .brand-name__dot {
    width: 26px; height: 26px; border-radius: 50%; background: var(--leaf-deep);
  }
  .brand-name__text {
    font-weight: 700; font-size: 34px; color: var(--stone);
  }

  .thc-ribbon {
    position: absolute; left: 556px; top: 0; width: 126px; height: 326px;
    background: var(--leaf);
    clip-path: polygon(0 0, 100% 0, 100% 100%, 50% 92%, 0 100%);
    display: flex; align-items: center; justify-content: center;
  }
  .thc-ribbon__text {
    writing-mode: vertical-rl; transform: rotate(180deg);
    display: flex; flex-direction: row; gap: 4px;
    color: var(--ink); line-height: 1; text-align: center;
  }
  .thc-ribbon__main { font-weight: 900; font-size: 50px; letter-spacing: 3px; }
  .thc-ribbon__sub { font-weight: 400; font-size: 34px; letter-spacing: 3px; }

  /* bottom black band content */
  .product {
    position: absolute; left: 128px; top: 368px; width: 649px; height: 619px;
    color: var(--paper); text-align: center;
  }
  .product > * { position: absolute; left: 0; width: 100%; white-space: nowrap; }
  .product__spectrum { top: 44px; font-weight: 700; font-size: 52px; letter-spacing: 4px; }
  .product__name { top: 138px; font-weight: 900; font-size: 92px; letter-spacing: 5px; color: var(--leaf); line-height: 1; }
  .product__strength { top: 266px; display: flex; justify-content: center; }
  .product__pill {
    background: var(--leaf); color: var(--ink);
    font-weight: 900; font-size: 44px; letter-spacing: 2px;
    padding: 2px 18px; border-radius: 14px; line-height: 1.2;
  }
  .product__type { top: 348px; font-weight: 400; font-size: 46px; letter-spacing: 2px; }
  .product__flavour {
    top: 442px; font-family: "Roboto Condensed", sans-serif;
    font-weight: 700; font-size: 40px; color: var(--leaf);
  }
  .product__volume { top: 528px; font-weight: 700; font-size: 40px; }
</style>
</head>
<body>
<main class="canvas">
  <section class="label" aria-label="Marbleleaf Hemp full spectrum hemp oil label">
    <div class="label__band-top">
      <div class="label__vertical label__vertical--hemp"><span>HEMP</span></div>
      <div class="label__divider"></div>
      <div class="brand-name">
        <span class="brand-name__dot"></span>
        <span class="brand-name__text">Marbleleaf Hemp</span>
      </div>
      <div class="thc-ribbon">
        <div class="thc-ribbon__text">
          <span class="thc-ribbon__main">THC</span>
          <span class="thc-ribbon__sub">FREE</span>
        </div>
      </div>
    </div>

    <div class="label__vertical label__vertical--brand"><span>MARBLELEAF</span></div>

    <div class="product">
      <p class="product__spectrum">FULL SPECTRUM</p>
      <h1 class="product__name">HEMP OIL</h1>
      <div class="product__strength"><span class="product__pill">PREMIUM • 2000MG</span></div>
      <p class="product__type">DIETARY SUPPLEMENT</p>
      <p class="product__flavour">Natural Peppermint Flavour</p>
      <p class="product__volume">1fl oz (30ml)</p>
    </div>
  </section>
</main>
</body>
</html>
```